Brantwell Group needs a business card design

We need a new business card design using the logo recently selected in a logo competition on Pixel Forum. Our business is a consultancy specializing in aviation and energy and the winning business card design will promote an image of precision and professionalism with creativity.

Please use the logo with the name on the front of the card and use a complementary font. Make the back white with either the light grey or dark grey logo.

Target Market(s)

Senior finance and legal leaders at aviation and energy companies

Industry/Entity Type

Management Consulting

Contact Information for Business Card

Peter Haldane
President
Brantwell Group

www.brantwellgroup.example

(555) 304-6198
ph@brantwellgroup.example

Requirements
Must have
• Professional font that goes well with the logo font

```html
<!DOCTYPE html>
<html lang="en">
<head>
<meta charset="utf-8">
<title>Brantwell Group — Business Card</title>
<link href="https://fonts.googleapis.com/css2?family=Arimo:wght@400;700&display=swap" rel="stylesheet">
<style>
  :root {
    --navy: #163f6b;
    --navy-text: #1d4a7a;
    --grey-text: #6d6f73;
    --card-white: #ffffff;
    --backdrop: #e7e5e1;
  }
  * { box-sizing: border-box; margin: 0; padding: 0; }
  html, body {
    width: 1200px; height: 950px; overflow: hidden;
    background: var(--backdrop);
    font-family: "Arimo", Arial, sans-serif;
  }
  .sheet {
    width: 1200px; height: 950px;
    display: flex; flex-direction: column; align-items: center; justify-content: center;
    gap: 50px;
  }
  .card {
    position: relative;
    width: 700px; height: 400px;
    box-shadow: 0 6px 18px rgba(0,0,0,0.18);
    overflow: hidden;
  }
  /* Card back */
  .card-back { background: var(--navy); color: #fff; }
  .card-back .wordmark {
    position: absolute; left: 0; right: 0; top: 140px;
    text-align: center;
    font-size: 34px; font-weight: 400; letter-spacing: 6px;
    text-transform: uppercase; color: #fff;
  }
  .card-back .web {
    position: absolute; left: 0; right: 0; bottom: 56px;
    text-align: center; font-size: 17px; letter-spacing: 3px; color: #fff;
  }
  /* Card front */
  .card-front { background: var(--card-white); }
  .corner-tab {
    position: absolute; left: 0; top: 74px;
    width: 24px; height: 44px;
  }
  .identity { position: absolute; left: 58px; top: 62px; }
  .identity .name { font-size: 25px; font-weight: 700; color: var(--navy-text); }
  .identity .title { font-size: 17px; color: var(--grey-text); margin-top: 4px; }
  .company {
    position: absolute; left: 140px; top: 178px;
    font-size: 17px; line-height: 23px; color: var(--grey-text);
  }
  .contacts {
    position: absolute; left: 140px; top: 262px;
    list-style: none; font-size: 17px; color: var(--grey-text);
  }
  .contacts li { display: flex; align-items: center; gap: 10px; height: 26px; }
  .contacts svg { width: 16px; height: 16px; flex: none; }
  .front-wordmark {
    position: absolute; right: 48px; top: 150px; width: 260px;
    text-align: center;
    font-size: 30px; font-weight: 400; letter-spacing: 4px; line-height: 44px;
    text-transform: uppercase; color: var(--navy-text);
  }
</style>
</head>
<body>
<main class="sheet">
  <section class="card card-back">
    <p class="wordmark">Brantwell Group</p>
    <p class="web">www.brantwellgroup.example</p>
  </section>

  <section class="card card-front">
    <svg class="corner-tab" viewBox="0 0 24 44" aria-hidden="true">
      <polygon points="0,0 24,22 0,44" fill="var(--navy)"/>
    </svg>
    <div class="identity">
      <p class="name">Peter J. Haldane</p>
      <p class="title">President</p>
    </div>
    <div class="company">
      <p>Brantwell Group LLC</p>
      <p>Finance and Strategy Consulting</p>
      <p>Aviation - Manufacturing - Energy</p>
    </div>
    <ul class="contacts">
      <li>
        <svg viewBox="0 0 16 16" aria-hidden="true"><path fill="var(--navy)" d="M3.5 1.5l2.5 0 1 3.5-1.6 1.2a8 8 0 0 0 4.4 4.4L11 9l3.5 1v2.5a1.5 1.5 0 0 1-1.5 1.5A11.5 11.5 0 0 1 2 3a1.5 1.5 0 0 1 1.5-1.5z"/></svg>
        <span>(555) 304-6198</span>
      </li>
      <li>
        <svg viewBox="0 0 16 16" aria-hidden="true"><rect x="1" y="3" width="14" height="10" rx="1" fill="var(--navy)"/><path d="M1.5 4l6.5 5 6.5-5" stroke="#fff" stroke-width="1.2" fill="none"/></svg>
        <span>ph@brantwellgroup.example</span>
      </li>
      <li>
        <svg viewBox="0 0 16 16" aria-hidden="true"><circle cx="8" cy="8" r="7" fill="var(--navy)"/><path d="M1 8h14M8 1c-3 3.5-3 10.5 0 14M8 1c3 3.5 3 10.5 0 14" stroke="#fff" stroke-width="1" fill="none"/></svg>
        <span>brantwellgroup.example</span>
      </li>
    </ul>
    <p class="front-wordmark">Brantwell Group</p>
  </section>
</main>
</body>
</html>
```